Flyer/Poster Tischtennis Sportverein
Zielgruppe
Tischtennisverein - Zielgruppe: Kinder von 8 - 12 Jahren
Aufgabenstellung
Allgemeiner Flyer für Tischtennisverein - Werbung für Kindertraining, Texbereich sollte im Design enthalten sein, aber so gestaltet dass der Text je nach Bedarf durch uns angepasst werden kann
DIN Format: Sollte als Postkartenformat sowie als DIN A3 oder DIN A2 Poster zu verwenden
Angehängtes Logo einbinden aber nicht zu prominent

```html
<!DOCTYPE html>
<html lang="de">
<head>
<meta charset="utf-8">
<title>SV Lindenbach – Tischtennis Poster</title>
<link href="https://fonts.googleapis.com/css2?family=Anton&family=Arimo:wght@400;700&display=swap" rel="stylesheet">
<style>
  :root {
    --club-red: #e3001b;
    --ink: #111111;
    --paper: #ffffff;
    --stage: #f2f2f2;
    --stripe-grey: #c9c9c9;
    --photo-dark: #1b1d1f;
    --photo-mid: #4a4f55;
    --photo-light: #8a9096;
  }
  * { margin: 0; padding: 0; box-sizing: border-box; }
  html, body { width: 1200px; height: 800px; overflow: hidden; }
  body { background: var(--stage); font-family: "Arimo", Arial, sans-serif; }
  .canvas { position: relative; width: 1200px; height: 800px; }
  .poster {
    position: absolute; top: 61px;
    width: 480px; height: 678px;
    background: var(--paper);
    border: 1px solid #333;
    overflow: hidden;
  }
  .poster--invite { left: 80px; }
  .poster--match { left: 640px; }
  .poster__art { position: absolute; inset: 0; width: 100%; height: 100%; }
  .club-name {
    position: absolute; top: 26px; left: 24px;
    color: var(--club-red); font-weight: 700; font-size: 15px;
  }
  .headline {
    position: absolute; left: 28px; top: 358px;
    font-family: "Anton", "Oswald", sans-serif;
    font-weight: 400; color: var(--club-red);
    font-size: 62px; line-height: 68px;
    letter-spacing: -0.5px;
    white-space: nowrap;
  }
  .body-copy {
    position: absolute; left: 28px; top: 520px; width: 414px;
    font-weight: 700; font-size: 11.8px; line-height: 13.4px;
    color: var(--ink);
  }
  .footer {
    position: absolute; left: 28px; top: 651px;
    font-size: 9px; color: #333;
  }
</style>
</head>
<body>
<main class="canvas">

  <article class="poster poster--invite">
    <svg class="poster__art" viewBox="0 0 554 782" preserveAspectRatio="none">
      <defs>
        <linearGradient id="photoToneA" x1="0" y1="0" x2="1" y2="1">
          <stop offset="0" stop-color="#8a9096"/>
          <stop offset="0.45" stop-color="#4a4f55"/>
          <stop offset="1" stop-color="#1b1d1f"/>
        </linearGradient>
      </defs>
      <polygon role="img" aria-label="Foto: Tischtennisspieler in Aktion vor dunkler Halle mit Netz und Ball" points="0,185 470,0 554,0 554,400 0,590" fill="url(#photoToneA)"/>
      <polygon points="0,172 440,0 470,0 0,185" fill="var(--stripe-grey)"/>
      <polygon points="0,285 420,110 554,70 554,95 0,320" fill="var(--club-red)"/>
      <polygon points="554,318 554,345 360,430 330,430" fill="var(--club-red)"/>
      <polygon points="0,590 554,400 554,412 0,604" fill="var(--stripe-grey)"/>
    </svg>
    <p class="club-name">SV Lindenbach</p>
    <h1 class="headline">Komm zum<br>Tischtennis</h1>
    <p class="body-copy">Olor as vellab inis soluptam, et laborum hillam dio. Ut est audic tet, veli­assum iliatus simaior recte coris velentione nobissim quae intiant ions­equi occusap ediciunt expliquati atiuriatem est, quam sitatisti qui que il ipsum ipsumquae sequistia as dolest, sandae laboreped milluptae non­seque dolo ipsusam quis solesci enihica borernatenis aut evel illibus aut ratente mpore, ut optatis quaerum eriae nimendi odi core verumqu odisquam ius eium rae. Nem quam exceria sintem quosse qui comnim num doluptae. Dit ex endi dem vent.</p>
    <p class="footer">SV Lindenbach 1921 e.V. | Am Mühlweg &nbsp;| &nbsp;61999 Lindenbach</p>
  </article>

  <article class="poster poster--match">
    <svg class="poster__art" viewBox="0 0 554 782" preserveAspectRatio="none">
      <defs>
        <linearGradient id="photoToneB" x1="0" y1="0" x2="1" y2="1">
          <stop offset="0" stop-color="#8a9096"/>
          <stop offset="0.45" stop-color="#4a4f55"/>
          <stop offset="1" stop-color="#1b1d1f"/>
        </linearGradient>
      </defs>
      <polygon role="img" aria-label="Foto: Tischtennisspieler in Aktion vor dunkler Halle mit Netz und Ball" points="0,185 470,0 554,0 554,400 0,590" fill="url(#photoToneB)"/>
      <polygon points="0,172 440,0 470,0 0,185" fill="var(--stripe-grey)"/>
      <polygon points="0,285 420,110 554,70 554,95 0,320" fill="var(--club-red)"/>
      <polygon points="554,318 554,345 360,430 330,430" fill="var(--club-red)"/>
      <polygon points="0,590 554,400 554,412 0,604" fill="var(--stripe-grey)"/>
    </svg>
    <p class="club-name">SV Lindenbach</p>
    <h1 class="headline">Das nächste<br>Spiel steht an</h1>
    <p class="body-copy">Olor as vellab inis soluptam, et laborum hillam dio. Ut est audic tet, veli­assum iliatus simaior recte coris velentione nobissim quae intiant ions­equi occusap ediciunt expliquati atiuriatem est, quam sitatisti qui que il ipsum ipsumquae sequistia as dolest, sandae laboreped milluptae non­seque dolo ipsusam quis solesci enihica borernatenis aut evel illibus aut ratente mpore, ut optatis quaerum eriae nimendi odi core verumqu odisquam ius eium rae. Nem quam exceria sintem quosse qui comnim num doluptae. Dit ex endi dem vent.</p>
    <p class="footer">SV Lindenbach 1921 e.V. | Am Mühlweg &nbsp;| &nbsp;61999 Lindenbach</p>
  </article>

</main>
</body>
</html>
```